Real estate business card

I need a business card for my real estate company. I help clients buy and sell properties. I would like to keep the design very simple and professional. I would like the design to convey professionalism, safety and trust. I prefer no graphics but a simple logo design would be nice if that is part of what you do.
Updates

Please keep the designs simple. No high-rise buildings please. 

Reason: My design has not been finalized.

Target Market(s)

Age group 30-60 mostly affluent

Industry/Entity Type

Real Estate

Contact Information for Business Card

Velmont Realtors
Howard Prisk, Broker
4153 Marlow Ave. #226, La Crescenta, CA 91207

Requirements
Nice to have
• Logo can be combination of my initials HP or just Z or a simple geometric shape? Please see "Desig Ideas" attachment. No pics of houses or shaking hands, dollar bills, $, %, etc...
Please use fonts similar to Helvetica for a clean, modern look (think Northern European design, simple, clean yet bold)

Also use font colors such as blue, grey in different shades. Use pastel colors if better.

```html
<!DOCTYPE html>
<html lang="en">
<head>
<meta charset="utf-8">
<title>Velmont Realtors – Business Card</title>
<link href="https://fonts.googleapis.com/css2?family=Roboto+Condensed:wght@400;700&display=swap" rel="stylesheet">
<style>
  :root {
    --backdrop: #e6e7ea;
    --card-white: #ffffff;
    --brand-blue: #2e3192;
    --accent-grey: #8a8c91;
    --text-white: #ffffff;
    --shadow: rgba(20, 22, 40, 0.22);
  }
  * { box-sizing: border-box; margin: 0; padding: 0; }
  html, body {
    width: 1200px;
    height: 1000px;
    overflow: hidden;
    background: var(--backdrop);
    font-family: "Roboto Condensed", Arial, sans-serif;
  }
  .sheet {
    position: relative;
    width: 1200px;
    height: 1000px;
  }
  .card {
    position: absolute;
    left: 280px;
    width: 640px;
    height: 366px;
    border-radius: 18px;
    background: var(--card-white);
    box-shadow: 0 8px 22px var(--shadow);
    overflow: hidden;
  }
  .card--front { top: 96px; }
  .card--back  { top: 538px; }

  .brand {
    position: absolute;
    left: 0;
    right: 0;
    display: flex;
    align-items: center;
    justify-content: center;
    gap: 16px;
    color: var(--brand-blue);
    font-weight: 700;
    letter-spacing: 2px;
    text-transform: uppercase;
  }
  .brand__square {
    width: 30px;
    height: 30px;
    background: var(--brand-blue);
  }
  .card--front .brand { top: 158px; font-size: 46px; }
  .card--back .brand { top: 58px; font-size: 38px; }
  .card--back .brand__square { width: 26px; height: 26px; }

  .back-bands {
    position: absolute;
    inset: 0;
    width: 100%;
    height: 100%;
  }
  .band--grey { fill: var(--accent-grey); }
  .band--blue { fill: var(--brand-blue); }

  .company-block {
    position: absolute;
    right: 34px;
    top: 196px;
    text-align: right;
    color: var(--text-white);
  }
  .company-block__name {
    font-weight: 700;
    font-size: 22px;
    letter-spacing: 0.5px;
    text-transform: uppercase;
  }
  .company-block__address {
    margin-top: 6px;
    font-size: 16px;
  }

  .person {
    position: absolute;
    left: 38px;
    bottom: 42px;
    color: var(--text-white);
  }
  .person__name {
    font-weight: 700;
    font-size: 22px;
    letter-spacing: 0.5px;
    text-transform: uppercase;
  }
  .person__title {
    margin-top: 4px;
    font-size: 18px;
  }
</style>
</head>
<body>
<main class="sheet">

  <section class="card card--front" aria-label="Card front">
    <div class="brand">
      <span class="brand__square" aria-hidden="true"></span>
      <span class="brand__name">Velmont Realtors</span>
    </div>
  </section>

  <section class="card card--back" aria-label="Card back">
    <svg class="back-bands" viewBox="0 0 640 366" preserveAspectRatio="none" aria-hidden="true">
      <path class="band--grey" d="M220 200 C 380 185, 520 130, 640 70 L 640 366 L 220 366 Z"/>
      <path class="band--blue" d="M0 205 C 180 225, 420 200, 640 95 L 640 366 L 0 366 Z"/>
    </svg>

    <div class="brand">
      <span class="brand__square" aria-hidden="true"></span>
      <span class="brand__name">Velmont Realtors</span>
    </div>

    <div class="company-block">
      <p class="company-block__name">Velmont Realtors</p>
      <p class="company-block__address">4153 Marlow Ave. #226, La Crescenta, CA 91207</p>
    </div>

    <div class="person">
      <p class="person__name">Howard Prisk</p>
      <p class="person__title">Broker</p>
    </div>
  </section>

</main>
</body>
</html>
```